The Brisk Hound - Dog Training Business Card Design

I need a business card design for a new dog training company based in Cronulla NSW called The Brisk Hound. I run puppy pre school classes, adult dog classes and do one on one training in the person's home.
I have studied for 2 years and use positive reinforcement training methods based on how dogs learn. I believe in communicating with our dogs what we want them to do rather than punish them for behaviours we don't like. I would like to see designs that use the colours that are used in my logo (please see attached)
I would like a simple and classic looking design. I don't want cartoon images of dogs or any animal images or drawings on the card. I have created my logo with this mindset. I am open to the subtle use of a dog's tail, paws or paw print.

Target Market(s)

high end area which is why I want a classic looking design
adults aged 25 and over

Industry/Entity Type

Dog Training

Contact Information for Business Card

Marisa Tolland
KOBRA Trained Professional Dog Trainer
www.thebriskhound-example.com.au
0437582061
marisa@thebriskhound-example.com.au

Font styles to use
Sans Serif

Colors
ffffff
86cae6
757575

Requirements
Must have
• Logo - I am trying to attach my logo and colour palette but it won't allow me. I will contact the company and upload ASAP.
Should not have
• images of dogs or cartoon drawings

```html
<!DOCTYPE html>
<html lang="en">
<head>
<meta charset="utf-8">
<title>The Brisk Hound – Business Card</title>
<link href="https://fonts.googleapis.com/css2?family=Questrial&display=swap" rel="stylesheet">
<style>
  :root {
    --page: #eeeeee;
    --white: #ffffff;
    --sky: #86cae6;
    --sky-soft: #aecfe5;
    --grey: #757575;
    --grey-light: #c4c4c4;
    --ink: #3a3a3a;
  }
  * { box-sizing: border-box; margin: 0; padding: 0; }
  html, body {
    width: 1200px; height: 1000px; overflow: hidden;
    background: var(--page);
    font-family: "Questrial", Arial, sans-serif;
  }
  .stage {
    width: 1200px; height: 1000px;
    display: flex; flex-direction: column;
    align-items: center; justify-content: center; gap: 60px;
  }
  .card {
    position: relative;
    width: 630px; height: 360px;
    overflow: hidden;
    box-shadow: 0 6px 18px rgba(0,0,0,0.15);
  }

  /* Contact side */
  .card--contact { background: var(--sky-soft); }
  .contact-band {
    position: absolute; left: 0; right: 0; top: 112px; height: 82px;
    background: var(--white);
  }
  .contact-name {
    position: absolute; right: 28px; top: 116px;
    font-size: 40px; letter-spacing: 2px; color: var(--sky);
  }
  .contact-title {
    position: absolute; right: 30px; top: 164px;
    font-size: 13.5px; letter-spacing: 0.4px; color: var(--ink);
  }
  .contact-list {
    position: absolute; left: 330px; top: 232px;
    list-style: none; color: var(--white);
    font-size: 16px; letter-spacing: 1px; line-height: 22px;
  }
  .contact-list li { display: flex; align-items: center; gap: 10px; }
  .contact-list svg { width: 14px; height: 14px; flex: none; }

  /* Brand side */
  .card--brand { background: var(--white); }
  .edge { position: absolute; top: 0; bottom: 0; width: 14px; background: var(--sky); }
  .edge--left { left: 0; }
  .edge--right { right: 0; }
  .brand {
    position: absolute; inset: 0;
    display: flex; flex-direction: column; align-items: center; justify-content: center;
  }
  .brand-line { display: flex; align-items: center; gap: 12px; }
  .brand-name { font-size: 44px; color: var(--grey-light); letter-spacing: 1px; }
  .brand-dot { width: 18px; height: 18px; border-radius: 50%; background: var(--sky); }
  .brand-tagline {
    margin-top: 6px; font-size: 12px; letter-spacing: 2.5px; color: var(--grey-light);
  }
</style>
</head>
<body>
<main class="stage">
  <section class="card card--contact" aria-label="Business card, contact side">
    <div class="contact-band"></div>
    <h1 class="contact-name">Marisa Tolland</h1>
    <p class="contact-title">KOBRA Trained Professional Dog Trainer</p>
    <ul class="contact-list">
      <li>
        <svg viewBox="0 0 14 14" aria-hidden="true"><rect width="14" height="14" rx="2" fill="#ffffff"/><path d="M4 3.5l2 0 .6 2-1.2.9a6 6 0 0 0 2.2 2.2l.9-1.2 2 .6 0 2A1 1 0 0 1 9.5 11 7 7 0 0 1 3 4.5 1 1 0 0 1 4 3.5z" fill="#aecfe5"/></svg>
        <span>0437582061</span>
      </li>
      <li>
        <svg viewBox="0 0 14 14" aria-hidden="true"><circle cx="7" cy="7" r="6" fill="none" stroke="#ffffff" stroke-width="1.3"/><path d="M1 7h12M7 1c-3 3-3 9 0 12M7 1c3 3 3 9 0 12" fill="none" stroke="#ffffff" stroke-width="1"/></svg>
        <span>www.thebriskhound-example.com.au</span>
      </li>
      <li>
        <svg viewBox="0 0 14 14" aria-hidden="true"><rect x="0.5" y="2.5" width="13" height="9" rx="1" fill="#ffffff"/><path d="M1 3l6 5 6-5" fill="none" stroke="#aecfe5" stroke-width="1.2"/></svg>
        <span>marisa@thebriskhound-example.com.au</span>
      </li>
    </ul>
  </section>

  <section class="card card--brand" aria-label="Business card, brand side">
    <div class="edge edge--left"></div>
    <div class="edge edge--right"></div>
    <div class="brand">
      <div class="brand-line">
        <span class="brand-name">The Brisk Hound</span>
        <span class="brand-dot"></span>
      </div>
      <p class="brand-tagline">POSITIVE TRAINING SPECIALIST</p>
    </div>
  </section>
</main>
</body>
</html>
```